VELINTA Promotions - Business Card Design Project

We are looking for a classy business cards for Promotion Company based in Toronto, Canada named Velinta Promotions.

Velinta Promotions has an idea and vision to set high standard, be EXCLUSIVE and attract a group of people that will follow us through events we promote (night clubs, brand promotions, music events, and sport events)

We want to present a high standards and classy image to the others...
Updates

Target Market(s)

male/female age 25-40 Target: business owners young entrepreneur - clubing industry - media industry - promotion industry - marketing media industry

Industry/Entity Type

Events

Requirements
Must have
• business cards should be classy, make people feel exclusive , make people react ..

```html
<!DOCTYPE html>
<html lang="en">
<head>
<meta charset="utf-8">
<title>Velinta Promotions – Business Card</title>
<link rel="stylesheet" href="https://fonts.googleapis.com/css2?family=Cinzel:wght@400;600&family=Questrial&display=swap">
<style>
  :root {
    --backdrop: #e9e3d9;
    --front-dark: #2b2b2b;
    --front-mid: #3a3a3a;
    --brand-cyan: #16b4e8;
    --back-cyan: #00b8ef;
    --ornament-light: #dcd6cc;
    --ornament-soft: #ece6dc;
    --white: #ffffff;
    --card-shadow: rgba(0, 0, 0, 0.35);
  }
  * { margin: 0; padding: 0; box-sizing: border-box; }
  html, body {
    width: 1200px;
    height: 1139px;
    overflow: hidden;
    background: var(--backdrop);
  }
  .canvas {
    position: relative;
    width: 1200px;
    height: 1139px;
  }
  .card {
    position: absolute;
    box-shadow: 0 6px 18px var(--card-shadow);
  }
  .card-front {
    left: 70px;
    top: 53px;
    width: 750px;
    height: 444px;
    background: linear-gradient(160deg, var(--front-mid), var(--front-dark));
  }
  .card-back {
    left: 387px;
    top: 552px;
    width: 749px;
    height: 430px;
    background: var(--back-cyan);
  }
  .ornament {
    position: absolute;
    border-radius: 48% 52% 40% 60% / 55% 45% 55% 45%;
  }
  .ornament-front {
    left: 234px;
    top: 23px;
    width: 494px;
    height: 228px;
    background: radial-gradient(ellipse at center, var(--ornament-light) 0%, rgba(220, 214, 204, 0.35) 60%, rgba(220, 214, 204, 0) 75%);
  }
  .ornament-side {
    left: 19px;
    top: 645px;
    width: 400px;
    height: 228px;
    background: radial-gradient(ellipse at center, var(--ornament-soft) 0%, rgba(236, 230, 220, 0.5) 55%, rgba(236, 230, 220, 0) 75%);
  }
  .brand {
    position: absolute;
    font-family: "Cinzel", serif;
    font-weight: 400;
    text-align: right;
    line-height: 1;
  }
  .brand-name { display: block; }
  .brand-tag { display: block; letter-spacing: 0.32em; }
  .brand-front {
    right: 82px;
    top: 283px;
    color: var(--brand-cyan);
  }
  .brand-front .brand-name { font-size: 88px; letter-spacing: 0.02em; }
  .brand-front .brand-tag { font-size: 24px; margin-top: 6px; margin-right: -8px; }
  .brand-back {
    right: 58px;
    top: 48px;
    color: var(--white);
  }
  .brand-back .brand-name { font-size: 42px; letter-spacing: 0.02em; }
  .brand-back .brand-tag { font-size: 12px; margin-top: 3px; margin-right: -4px; }
  .contact {
    position: absolute;
    left: 36px;
    right: 44px;
    bottom: 28px;
    display: flex;
    justify-content: space-between;
    font-family: "Questrial", sans-serif;
    font-size: 20px;
    color: var(--white);
    list-style: none;
  }
</style>
</head>
<body>
  <main class="canvas">
    <div class="ornament ornament-side" role="img" aria-label="Pale floral swirl ornament beside the back of the card"></div>

    <section class="card card-front" aria-label="Card front">
      <div class="ornament ornament-front" role="img" aria-label="Light floral flourish ornament across the top of the card"></div>
      <h1 class="brand brand-front">
        <span class="brand-name">VELINTA</span>
        <span class="brand-tag">PROMOTIONS</span>
      </h1>
    </section>

    <section class="card card-back" aria-label="Card back">
      <p class="brand brand-back">
        <span class="brand-name">VELINTA</span>
        <span class="brand-tag">PROMOTIONS</span>
      </p>
      <ul class="contact">
        <li class="contact-email">name@velinta.com</li>
        <li class="contact-address">1 street, town, code</li>
        <li class="contact-phone">+1 416 555 0182</li>
      </ul>
    </section>
  </main>
</body>
</html>
```